business card and flyer/pricelist

Business Name: Willow Strand Salon
new boutique salon run from home, using Australian owned natural products and colours, we need a flyer design to do a letter box drop to advertise the business as well as incorporating a price list on the front (single sided with writing on front and only colour on back)

The salon has a natural feel with light coloured timber chairs, bamboo timber bench top and shelving.

we are after a natural toned colour for the flyer, with possibly a brown/darkish colour writing

we are after a flyer that will also be able to use the design heading (business name) for business cards as well

feel free to look on my pintrest account to get a feel for my style under Corinne Belvane.

I love simple clean and Natural looks.

Industry/Entity Type

Boutique

Font styles to use
Script
Other font styles liked:
• SCRIPT HANDWRITTEN FONTS

Colors
cadf82
e9f1ce
5c5c5c
d3d3d3
add136
fee18a

Requirements
Must have
• NATURAL COLOURINGS, eg soft greens, browns,
white or off white background.
Should not have
• photos,

```html
<!DOCTYPE html>
<html lang="en">
<head>
<meta charset="utf-8">
<title>Willow Strand Salon – Flyer and Price List</title>
<link href="https://fonts.googleapis.com/css2?family=Federo&family=Pinyon+Script&family=Open+Sans:wght@400;600;700&display=swap" rel="stylesheet">
<style>
  :root{
    --stage:#3b2b20;
    --wood-light:#f6deaa;
    --wood-mid:#ecc987;
    --wood-tan:#d4a863;
    --brown-title:#8a5a34;
    --brown-dark:#3b2117;
    --brown-text:#7a4a24;
    --panel-black:#0b0b0a;
    --panel-gold:#b98a3c;
    --script-green:#b6d43a;
    --row-brown:#6b3f22;
    --row-brown-hi:#96623a;
    --row-green:#add136;
    --white:#ffffff;
    --ink:#2d2d2d;
    --ivory:#f1ece0;
  }
  *{box-sizing:border-box;margin:0;padding:0}
  html,body{width:1200px;height:1112px;overflow:hidden}
  body{background:var(--stage);font-family:"Open Sans",Arial,sans-serif;position:relative}

  .flyer{
    position:absolute;top:93px;width:438px;height:945px;overflow:hidden;
    background:linear-gradient(100deg,var(--wood-light) 0%,var(--wood-mid) 45%,var(--wood-light) 70%,var(--wood-mid) 100%);
    box-shadow:0 6px 18px rgba(0,0,0,.45);
  }
  .flyer--front{left:124px}
  .flyer--back{left:606px}

  .flyer--front .base-band{
    position:absolute;left:0;top:690px;width:100%;height:255px;
    background:linear-gradient(180deg,rgba(212,168,99,0) 0%,var(--wood-tan) 60%);
  }

  .brand-title{
    position:absolute;top:40px;left:0;width:100%;text-align:center;
    font-family:"Federo",sans-serif;font-size:50px;line-height:58px;
    color:var(--brown-title);letter-spacing:1px;text-transform:uppercase;
  }

  .price-panel{position:absolute;left:45px;top:185px;width:347px;height:523px}
  .flyer--front .price-panel{background:var(--panel-black);border:2px solid var(--panel-gold)}
  .flyer--back .price-panel{left:46px;top:367px;width:345px;height:523px;background:var(--brown-dark);border:2px solid var(--wood-mid)}

  .price-title{
    position:absolute;top:30px;width:100%;text-align:center;
    font-family:"Pinyon Script",cursive;font-size:46px;font-weight:400;color:var(--script-green);line-height:1;
  }
  .flyer--back .price-title{top:28px}

  .price-rows{position:absolute;left:24px;top:106px;display:flex;flex-direction:column;gap:6px;list-style:none}
  .price-row{display:flex;height:25px}
  .service{
    width:213px;border-radius:13px 0 0 13px;padding-left:14px;
    background:linear-gradient(90deg,var(--row-brown) 0%,var(--row-brown-hi) 55%,var(--row-brown) 100%);
    color:var(--white);font-size:15px;font-weight:600;line-height:25px;white-space:nowrap;
  }
  .price{
    width:72px;border-radius:0 13px 13px 0;padding-left:12px;
    background:var(--row-green);color:var(--ink);font-size:15px;font-weight:600;line-height:25px;
  }

  .panel-photo{
    position:absolute;left:14px;bottom:12px;width:250px;height:128px;
    background:linear-gradient(90deg,#5a3520 0%,#8a5a34 50%,#2a1a10 100%);
  }
  .flower-art{
    position:absolute;left:262px;top:600px;width:176px;height:180px;border-radius:14px;
    background:linear-gradient(160deg,#a9cc5a 0%,#e4ecc8 35%,var(--ivory) 70%);
  }

  .contact-card{
    position:absolute;left:41px;top:757px;width:342px;height:163px;border-radius:12px;
    background:rgba(255,255,255,.82);padding:14px 16px;color:var(--ink);
  }
  .contact-card .name{font-family:"Federo",sans-serif;font-size:22px;color:var(--brown-text);text-transform:uppercase}
  .contact-card .owner{margin-top:12px;font-weight:700;font-size:14px;color:var(--brown-text)}
  .contact-card p{font-size:12.5px;line-height:18px}
  .contact-card .label{color:var(--brown-text)}
  .contact-card .phone{margin-top:4px;font-size:13px;color:var(--brown-text)}
  .contact-card .phone strong{font-size:18px}

  .hero-photo{
    position:absolute;left:70px;top:0;width:298px;height:367px;
    background:linear-gradient(180deg,#6b4128 0%,#a0704a 55%,#c99a6c 100%);
  }

  .back-info{position:absolute;left:0;top:400px;width:100%;text-align:center;color:var(--white)}
  .back-info .name{font-family:"Federo",sans-serif;font-size:26px;text-transform:uppercase;letter-spacing:.5px}
  .back-info .owner{margin-top:14px;font-weight:700;font-size:14px}
  .back-info p{font-size:12.5px;line-height:18px}

  .call-line{position:absolute;left:26px;top:905px;color:var(--white);font-size:12.5px;white-space:nowrap}
  .call-line strong{font-size:27px;color:var(--brown-dark);margin-left:6px;vertical-align:-4px;font-weight:700}
</style>
</head>
<body>

<section class="flyer flyer--front">
  <div class="base-band"></div>

  <h1 class="brand-title">Willow Strand<br>Salon</h1>

  <div class="price-panel">
    <h2 class="price-title">Price List</h2>
    <ul class="price-rows">
      <li class="price-row"><span class="service">Service Packname1</span><span class="price">$00</span></li>
      <li class="price-row"><span class="service">Service packname1</span><span class="price">$00</span></li>
      <li class="price-row"><span class="service">Service packname1</span><span class="price">$00</span></li>
      <li class="price-row"><span class="service">Service packname1</span><span class="price">$00</span></li>
      <li class="price-row"><span class="service">Service packname1</span><span class="price">$00</span></li>
      <li class="price-row"><span class="service">Service packname1</span><span class="price">$00</span></li>
      <li class="price-row"><span class="service">Service packname1</span><span class="price">$00</span></li>
      <li class="price-row"><span class="service">Service packname1</span><span class="price">$00</span></li>
      <li class="price-row"><span class="service">Service packname1</span><span class="price">$00</span></li>
    </ul>
    <div class="panel-photo" role="img" aria-label="Photo area: woman in profile with long flowing brown hair"></div>
  </div>

  <div class="flower-art" role="img" aria-label="Illustration area: white lily with a green leaf"></div>

  <div class="contact-card">
    <div class="name">Willow Strand Salon</div>
    <div class="owner">Owners Name here</div>
    <p>Brookfield Name, Suite 0000,</p>
    <p>Cityname, Country name, Pin-0000.</p>
    <p><span class="label">Email:</span> info@willowstrandsalon.com</p>
    <div class="phone">Contact Us: <strong>012 345 6789</strong></div>
  </div>
</section>

<section class="flyer flyer--back">
  <div class="hero-photo" role="img" aria-label="Photo area: portrait of a woman with sleek brown hair"></div>

  <div class="price-panel">
    <h2 class="price-title">Price List</h2>
    <ul class="price-rows">
      <li class="price-row"><span class="service">Service Packname1</span><span class="price">$00</span></li>
      <li class="price-row"><span class="service">Service packname1</span><span class="price">$00</span></li>
      <li class="price-row"><span class="service">Service packname1</span><span class="price">$00</span></li>
      <li class="price-row"><span class="service">Service packname1</span><span class="price">$00</span></li>
      <li class="price-row"><span class="service">Service packname1</span><span class="price">$00</span></li>
      <li class="price-row"><span class="service">Service packname1</span><span class="price">$00</span></li>
      <li class="price-row"><span class="service">Service packname1</span><span class="price">$00</span></li>
      <li class="price-row"><span class="service">Service packname1</span><span class="price">$00</span></li>
      <li class="price-row"><span class="service">Service packname1</span><span class="price">$00</span></li>
    </ul>
    <div class="back-info">
      <div class="name">Willow Strand Salon</div>
      <div class="owner">Owners Name here</div>
      <p>Brookfield Name, Suite 0000,</p>
      <p>Cityname, Country name, Pin-0000.</p>
      <p>Email: info@willowstrandsalon.com</p>
    </div>
  </div>

  <div class="call-line">For more information please call : <strong>012 345 6789</strong></div>
</section>

</body>
</html>
```